Office brochure for chronic pain doctor

I need an brochure for my office, and since I want to be able to mail the brochure, I think trifold would be the best size. I treat patients with chronic head and neck pain, as well as sleep apnea. I treat all of the following:

1. headaches
2. myofascial pain, which is a fancy way of saying muscle pain
3. neuropathic pain, which is a fancy way of saying nerve pain
4. TMJ, which stands for the temporomandibular joint (jaw joint)
5. obstructive sleep apnea

The colors will be based on my logo on my website, which you can see at www.BrightKVZ.net, and you can learn more about what I do at my website. KVZ stands for orofacial pain, which is a speciality training within the field of dentistry but I do not treat teeth. I have high resolution graphics for the brochure so I need someone with an artistic eye to design and lay out the brochure.

The logo colors are:
Purple 9e80bb
Pink f6b1d0
Blue 0f4b8f
Updates

I had a request for the logo in a .ai or .pdf format, which I have just uploaded. Please let me know if you have any other requests. Thank you, Tomas

Target Market(s)

80% female, 20% male. I am in an upscale area of Los Angeles called Beverly Hills but I will see a patient from any area around Los Angeles or from any area in the world.

Industry/Entity Type

Training

Colors
6b449b
e567a6
0355a3

Requirements
Must have
• I want a small section of the brochure to feature each of the five areas I treat, and I have included an image to place in each of the five sections. A small section should include a short bio of me, which you can condense from www.brightkvz.net/tomas. The brochure must appeal to women since 80% of my patients are female but I don't want to completely ignore men. Most of the pain patients are female, and most of the sleep apnea patients are male.

Here are the colors in my logo
Purple 9e80bb
Pink f6b1d0
Blue 0f4b8f
Should not have
• Anything related to teeth or dentistry.
No decorative or script fonts.

```html
<!DOCTYPE html>
<html lang="en">
<head>
<meta charset="utf-8">
<title>Conditions We Treat – Brochure Inside Panel</title>
<link href="https://fonts.googleapis.com/css2?family=Fira+Sans:wght@300;400&display=swap" rel="stylesheet">
<style>
  :root {
    --navy: #0c2a6b;
    --heading: #13357a;
    --text: #231f20;
    --pink-soft: #f7d3e4;
    --pink-frame: #f2a9cb;
    --white: #ffffff;
  }
  * { box-sizing: border-box; margin: 0; padding: 0; }
  html, body { width: 1200px; height: 848px; overflow: hidden; }
  body {
    position: relative;
    font-family: "Fira Sans", Arial, sans-serif;
    font-weight: 400;
    color: var(--text);
    background: linear-gradient(to bottom, var(--white) 0%, var(--white) 45%, var(--pink-soft) 100%);
  }
  .top-band {
    position: absolute; left: 0; top: 0; width: 1200px; height: 27px;
    background: var(--navy);
  }
  .column {
    position: absolute; top: 114px; width: 342px;
  }
  .column--left { left: 30px; }
  .column--middle { left: 430px; }
  .column--right { left: 828px; }
  .topic { margin-bottom: 14px; }
  .topic h2 {
    font-weight: 300; font-size: 36px; line-height: 1; color: var(--heading);
    margin-bottom: 16px; letter-spacing: 0.2px;
  }
  .topic p, .topic li, .topic h3 {
    font-size: 12.6px; line-height: 16.6px;
  }
  .topic p + p { margin-top: 12px; }
  .topic-image {
    float: left; margin: 0 13px 6px 0;
    border: 2px solid var(--pink-frame); border-radius: 6px;
  }
  .topic-image--portrait { width: 124px; height: 162px; background: linear-gradient(160deg, #f3e6df, #e4c3b2 60%, #c98a6a); }
  .topic-image--neuro { width: 124px; height: 162px; background: linear-gradient(160deg, #f5e8e2, #e2bca8 60%, #b58268); }
  .topic-image--muscle { width: 124px; height: 162px; background: linear-gradient(160deg, #f1dcd0, #c96a55 55%, #8e3a2c); }
  .topic-image--joint { width: 134px; height: 124px; background: linear-gradient(150deg, #efe6cf, #d9c79a 50%, #a94a3a); }
  .topic-image--sleep { width: 134px; height: 113px; background: linear-gradient(160deg, #f7f1ee, #e8c9bc 55%, #9c5a44); }
  .topic h3 { font-weight: 400; margin-top: 12px; }
  .topic ul { list-style: none; }
  .topic li { position: relative; padding-left: 12px; }
  .topic li::before { content: "•"; position: absolute; left: 0; }
  .topic--tmjd { margin-top: 14px; }
</style>
</head>
<body>
  <div class="top-band"></div>

  <div class="column column--left">
    <section class="topic">
      <h2>Headaches</h2>
      <div class="topic-image topic-image--portrait" role="img" aria-label="Illustration of a woman's head with headache pain area highlighted in red"></div>
      <p>A headache is an ache or pain occurring anywhere in the face, neck or head. Headache pain is experienced through pain-sensitive structures around the head and neck including blood vessels, nerves, muscles and tissues including the eyes, ears and sinuses. Headaches can range across the intensity spectrum from mild, tolerable pain to severe pain that prohibits daily activities. Headaches are one of the most commonly experienced causes of pain. They can be occasional, recurrent or chronic in frequency.</p>
    </section>
    <section class="topic">
      <h2>Myofascial Pain</h2>
      <div class="topic-image topic-image--muscle" role="img" aria-label="Anatomical illustration of the muscles of the head and neck"></div>
      <p>Chronic myofascial pain (CMP) is a chronic pain disease characterized by trigger points in the musculature causing pain in distinct areas of the body. Pain symptoms of CMP can be severe and debilitating. While much of the underlying mechanics of myofascial pain is not clearly understood, research suggests that symptoms are derived from the existence of trigger points within muscles, which are activated by injury or repetitive strain to muscles. It is generally understood that while one trigger point may be responsible for an experience of myofascial pain, it is more commonly a network of several trigger points that contribute to pain in a given region.</p>
    </section>
  </div>

  <div class="column column--middle">
    <section class="topic">
      <h2>Neuropathic Pain</h2>
      <div class="topic-image topic-image--neuro" role="img" aria-label="Illustration of a face showing nerve pain points"></div>
      <p>Neuropathic pain disorders are a set of pain conditions resulting from disorder or injury to the nervous system. The human nervous system is divided into two general parts: the central nervous system, comprising the brain and spinal cord, and the peripheral nervous system, including nerves that go to the limbs, trunk, face and all outlying areas of the body. When nerves of the peripheral system sense pain from mechanical, chemical or thermal sensations, they relay the sensation to the central nervous system for processing. Additionally, the spine and brain command a network a nerves conducting sensation along the back, neck, head and face.</p>
    </section>
    <section class="topic topic--tmjd">
      <h2>TMJD</h2>
      <div class="topic-image topic-image--joint" role="img" aria-label="Anatomical illustration of the jaw joint and surrounding muscle"></div>
      <p>Temporomandibular joint disorder, also known as TMJ, TMD, or TMJD, is a general term covering any disorder causing inflammation of the temporomandibular joint, which connects the skull to the mandible. There are a number of conditions that can cause pain in the jaw joint and the muscles involved in the closing and opening of the jaw. Disorders affecting the temporomandibular joint can affect a person's ability to eat, speak, swallow, chew, and breathe.</p>
      <h3>A person suffering from TMJD may experience:</h3>
      <ul>
        <li>Clicking or popping noise in the jaw</li>
        <li>Neck pain, shoulder pain, back pain or headaches</li>
        <li>Ringing in the ears or decreased hearing</li>
        <li>Dizziness and vision problem</li>
      </ul>
    </section>
  </div>

  <div class="column column--right">
    <section class="topic">
      <h2>Sleep Apnea</h2>
      <div class="topic-image topic-image--sleep" role="img" aria-label="Illustration of a sleeping woman with the blocked airway highlighted"></div>
      <p>Sleep apnea is a common sleeping disorder marked by shallow breathing, pauses in breath and labored breathing punctuated by gasping or snoring sounds. Pauses of breath can last from several seconds up to minutes and can happen from five to thirty times or more per hour. A pause may be followed by a choking or snorting sound as the sleeper involuntarily gasps for breath.</p>
      <p>The two main causes of sleep apnea are a blockage of the airway and poor signals from the part of the brain responsible for directing the muscles that control breathing. These two causes may occur together, however sleep apnea caused by a collapsed or blocked airway, known as obstructive sleep apnea, is the most common reason sleep apnea is experienced.</p>
      <p>As oxygen is restricted to the lungs, blood and brain, the sleeper is less likely to fall into deep, restorative cycles of sleep. A person suffering from sleep apnea finds himself or herself tired during the day as the disorder inhibits restful sleep. A lack of quality sleep can lead to accidents or poor job performance. Serious health concerns including heart disease, high blood pressure, stroke, diabetes and depression can also result from untreated sleep apnea.</p>
    </section>
  </div>
</body>
</html>
```